Bellwether Recovery Brochure for a drug and alcohol addiction treatment center.

***Update #2***
For graphic highlights no intrusion into text and no fade into adjoining areas.Use modern clean white layout with grey and light orange color scheme. Use attached yoga photo and other photos. For cover try moving number and logo around, and also try with cover photo not full size. Also use larger text with bullet points in a couple spots. Also try with new attached cover photos.
***Update*** I have attached some new photos to clarify the design wanted. My client likes the size (but not design) of the brochure in the newly included photos. Note the measurements - when closed it is 6" wide x 7" tall. When fully open it is 18" long, 7" wide, with 2 folds. I apologize if my terminology below was confusing. Please confirm that your design reflects the desired layout, and please modify your design if it does not. Thanks!
Want a trifold brochure 6" wide x 7" height. Design is for a drug and alcohol addiction treatment center. We want clean, soft, contemporary with highlight colors orange and grey, with contemporary font. Maybe some soft curves on design - see this A4 design we like but not the colors:
http://quillstockmart.net/item/business-trifold-brochure-wave/7315920?s_phrase=trifold%20business%20brochure&s_rank=54
See company web site for style cues and some content you can use:
http://bellwetherrecovery.com/
You can use the attached photos and logo in the design. Try sun in hand photo on cover, or man on beach. Please do not use the words "The Bellwether Recovery Center" in verbiage or titles, for business reasons we want to use "Bellwether Recovery Center" with no "The" instead.
Please note that the logo has been updated. The new logo is attached below. Use bellwether rev2.png for logo.
Addiction treatment industry professionals; family and decision makers of addict; addict themselves.

```html
<!DOCTYPE html>
<html lang="en">
<head>
<meta charset="utf-8">
<title>Bellwether Recovery Center – Trifold Brochure</title>
<link href="https://fonts.googleapis.com/css2?family=Roboto:wght@300;400;700&display=swap" rel="stylesheet">
<style>
  :root {
    --stage: #e6e6e6;
    --paper: #ffffff;
    --orange: #f26f21;
    --orange-light: #f7941d;
    --ink: #111111;
    --body-grey: #555555;
    --wash-grey: #ececec;
  }
  html, body {
    margin: 0;
    padding: 0;
    width: 1200px;
    height: 900px;
    overflow: hidden;
    background: var(--stage);
    font-family: "Roboto", Arial, sans-serif;
  }
  .canvas { position: relative; width: 1200px; height: 900px; }
  .spread {
    position: absolute;
    left: 55px; top: 238px;
    width: 1090px; height: 424px;
    background: var(--paper);
    overflow: hidden;
  }
  .spread-art { position: absolute; inset: 0; }
  .about {
    position: absolute;
    left: 27px; top: 24px;
    width: 308px;
  }
  .about-title {
    margin: 0 0 9px;
    text-align: center;
    font-weight: 400;
    font-size: 16.5px;
    color: var(--orange);
  }
  .about p {
    margin: 0 0 8px;
    font-size: 8.4px;
    line-height: 11.6px;
    color: var(--body-grey);
  }
  .brand-name {
    position: absolute;
    text-align: center;
    font-weight: 700;
    color: var(--ink);
    line-height: 1;
    letter-spacing: 0.3px;
  }
  .brand-name span { display: block; }
  .brand-name--contact { left: 363px; width: 363px; top: 128px; font-size: 17px; }
  .brand-name--contact span + span { font-size: 10px; margin-top: 3px; }
  .brand-name--cover { left: 727px; width: 300px; top: 118px; font-size: 21px; }
  .brand-name--cover span + span { font-size: 12px; margin-top: 3px; }
  .contact {
    position: absolute;
    left: 363px; width: 363px; top: 171px;
    text-align: center;
  }
  .contact-phone { margin: 0; font-size: 16.5px; color: var(--orange); }
  .contact-address { margin: 5px 0 0; font-size: 9.5px; color: #333; }
  .contact-web { margin: 10px 0 0; font-size: 9.5px; color: #333; letter-spacing: 1.6px; }
  .cover-headline {
    position: absolute;
    left: 755px; top: 258px;
    margin: 0;
    color: #fff;
    font-weight: 300;
    line-height: 1;
  }
  .cover-headline span { display: block; }
  .cover-headline .lead { font-size: 21px; letter-spacing: 0.5px; font-weight: 400; }
  .cover-headline .main { font-size: 59px; margin-top: 2px; letter-spacing: -0.5px; }
</style>
</head>
<body>
<main class="canvas">
  <section class="spread" aria-label="Bellwether Recovery Center trifold brochure, open spread">
    <svg class="spread-art" viewBox="0 0 1090 424" width="1090" height="424" aria-hidden="false">
      <defs>
        <linearGradient id="wash" x1="0" y1="0" x2="1" y2="0">
          <stop offset="0" stop-color="#f4f4f4"/>
          <stop offset="1" stop-color="#e2e2e2"/>
        </linearGradient>
        <linearGradient id="sunset-hand" x1="0" y1="0" x2="0" y2="1">
          <stop offset="0" stop-color="#e88a1e"/>
          <stop offset="0.45" stop-color="#c9651a"/>
          <stop offset="1" stop-color="#4a2a14"/>
        </linearGradient>
        <linearGradient id="sunset-yoga" x1="0" y1="0" x2="0" y2="1">
          <stop offset="0" stop-color="#e7c2c9"/>
          <stop offset="0.4" stop-color="#c89aa6"/>
          <stop offset="0.6" stop-color="#7d5e78"/>
          <stop offset="1" stop-color="#3b2a3c"/>
        </linearGradient>
        <radialGradient id="map-tones" cx="0.5" cy="0.5" r="0.6">
          <stop offset="0" stop-color="#e7e3cf"/>
          <stop offset="0.7" stop-color="#cfdcb8"/>
          <stop offset="1" stop-color="#a9c9e6"/>
        </radialGradient>
      </defs>

      <rect class="photo-wash" x="0" y="0" width="363" height="300" fill="url(#wash)" role="img" aria-label="Faded greyscale photo of a counselling conversation"/>
      <rect class="photo-wash" x="363" y="0" width="300" height="324" fill="url(#wash)" role="img" aria-label="Faded greyscale photo of a smiling couple"/>

      <path class="photo-cover" d="M727,0 H1090 V424 H727 Z" fill="url(#sunset-yoga)" role="img" aria-label="Photo of a woman meditating in a yoga pose on a beach at sunset"/>

      <path class="wave-light" d="M0,258 C150,240 300,244 450,290 C600,336 700,372 800,362 C900,353 1000,335 1090,316 L1090,424 L0,424 Z" fill="var(--orange-light)"/>
      <path class="wave-main" d="M0,268 C150,250 300,254 450,300 C600,346 700,382 800,372 C900,363 1000,345 1090,326 L1090,424 L0,424 Z" fill="var(--orange)"/>

      <path class="photo-hand" d="M0,284 C110,268 250,266 363,282 L363,424 L0,424 Z" fill="url(#sunset-hand)" role="img" aria-label="Photo of a hand holding the setting sun over the sea"/>

      <circle cx="542" cy="327" r="75" fill="var(--orange-light)"/>
      <circle cx="542" cy="327" r="68" fill="url(#map-tones)" role="img" aria-label="Map showing the center's location in Southern California"/>
    </svg>

    <article class="about">
      <h2 class="about-title">About Bellwether Recovery Center</h2>
      <p>At Bellwether Recovery Center we believe strongly in providing the highest possible levels of care for you or your loved one. We have brought together some of the best and most experienced people in the industry to form our treatment team.</p>
      <p>In addition, Bellwether Recovery Center facilities are comprehensive and spacious, and offer comfortable accommodations that make the process of alcohol rehab or drug rehab less stressful. Bellwether Recovery Center photo gallery provides some images of our campus, where you or your loved one will find release from the enslavement of alcoholism or drug addiction.</p>
      <p>Feel free to fill out our online form to verify your insurance. You can also fill out the form on our financing page to begin the easy process of applying for financing help. We hope to hear from you, and someone is always available to provide the help that you or your loved one requires. Call Bellwether Recovery Center at 800-555-0148 today!</p>
    </article>

    <div class="brand-name brand-name--contact"><span>BELLWETHER</span><span>RECOVERY CENTER</span></div>

    <div class="contact">
      <p class="contact-phone">Call Us at 800-555-0148</p>
      <p class="contact-address">2240 Harbor View Ave, Larkspur Bay, CA 90017, USA</p>
      <p class="contact-web">www.bellwetherrecovery.com</p>
    </div>

    <div class="brand-name brand-name--cover"><span>BELLWETHER</span><span>RECOVERY CENTER</span></div>

    <h1 class="cover-headline"><span class="lead">RECOVER FROM</span><span class="main">ADDICTION</span></h1>
  </section>
</main>
</body>
</html>
```